Total Health and Wellness Infographic

Hello,
We need an infographic of the 16 factors for total health and wellness.  We are imagining a circle pie chart with all 16 categories, with each pie having a corresponding graphic in it.
We want it to be modern, beautiful, easy to understand (we welcome cartoon graphics)
The 16 points are:
a. Sleep
b. Exercise/Movement
c. Macronutrient Diet
d. Micronutrients
e. Health Habits (Tracking, Morning Routines, Mindfulness/Meditation)
f. CV Health
g. GI Health
h. Brain Health
i. Inflammation (Food allergies, etc)
j. Hormone Health
k. Stress
l. Immunity and Cancer Detection/ Prevention
m. Detoxification – heavy metals, pesticides, your environment
n. Longevity
o. Sexual Health
p. Aesthetics – Facial, Hair, Body
Attached are our brand standards for reference.
Let us know if you have any questions.
Thank you!

```html
<!DOCTYPE html>
<html lang="en">
<head>
<meta charset="utf-8">
<title>16 Factors for Total Health and Wellness</title>
<link href="https://fonts.googleapis.com/css2?family=Lato:wght@300;700&display=swap" rel="stylesheet">
<style>
  :root {
    --sky-top: #5cc6f0;
    --sky-mid: #2e85a2;
    --sky-bottom: #2d587b;
    --ink-light: #ffffff;
    --slice-a: rgba(255, 255, 255, 0.07);
    --slice-b: rgba(255, 255, 255, 0.15);
    --icon-fill: rgba(255, 255, 255, 0.24);
    --hub-fill: #2c6f8e;
  }
  html, body {
    margin: 0;
    padding: 0;
    overflow: hidden;
  }
  .poster {
    position: relative;
    width: 928px;
    height: 1200px;
    overflow: hidden;
    background: linear-gradient(180deg, var(--sky-top) 0%, #41a5cf 22%, var(--sky-mid) 52%, #2c6f8e 72%, var(--sky-bottom) 100%);
    font-family: 'Lato', sans-serif;
    color: var(--ink-light);
  }
  .poster-title {
    position: absolute;
    top: 128px;
    left: 0;
    width: 928px;
    margin: 0;
    text-align: center;
    font-weight: 300;
    font-size: 33px;
    letter-spacing: -0.2px;
  }
  .title-rule {
    position: absolute;
    top: 182px;
    left: 109px;
    width: 709px;
    height: 2px;
    background: var(--ink-light);
  }
  .factor-wheel {
    position: absolute;
    top: 0;
    left: 0;
  }
  .slice { stroke: var(--ink-light); stroke-width: 2; }
  .slice-a { fill: var(--slice-a); }
  .slice-b { fill: var(--slice-b); }
  .factor-icon { fill: var(--icon-fill); stroke: var(--ink-light); stroke-width: 1.5; }
  .factor-label {
    fill: var(--ink-light);
    font-family: 'Lato', sans-serif;
    font-weight: 700;
    font-size: 10.5px;
    letter-spacing: 1px;
  }
  .wheel-hub { fill: var(--hub-fill); stroke: var(--ink-light); stroke-width: 2; }
  .brand-name {
    position: absolute;
    top: 1006px;
    left: 0;
    width: 928px;
    text-align: center;
    font-weight: 300;
    font-size: 56px;
    letter-spacing: 1px;
  }
</style>
</head>
<body>
  <main class="poster">
    <h1 class="poster-title">16 FACTORS FOR TOTAL HEALTH AND WELLNESS</h1>
    <div class="title-rule"></div>

    <svg class="factor-wheel" width="928" height="1200" viewBox="0 0 928 1200" role="group" aria-label="Pie chart of the 16 factors">
      <defs>
        <path id="slice-shape" d="M -11.71 -58.85 L -64.38 -323.66 A 330 330 0 0 1 64.38 -323.66 L 11.71 -58.85 A 60 60 0 0 0 -11.71 -58.85 Z"/>
      </defs>
      <g transform="translate(464 600)">
        <g transform="rotate(11.25)"><use href="#slice-shape" class="slice slice-a"/><circle class="factor-icon" cx="0" cy="-285" r="24" role="img" aria-label="Sleep icon: moon and stars"/><text class="factor-label" x="0" y="-175" text-anchor="middle" dominant-baseline="central" transform="rotate(-90 0 -175)">SLEEP</text></g>
        <g transform="rotate(33.75)"><use href="#slice-shape" class="slice slice-b"/><circle class="factor-icon" cx="0" cy="-285" r="24" role="img" aria-label="Exercise icon: running figure"/><text class="factor-label" x="0" y="-175" text-anchor="middle" dominant-baseline="central" transform="rotate(-90 0 -175)">EXERCISE/MOVEMENT</text></g>
        <g transform="rotate(56.25)"><use href="#slice-shape" class="slice slice-a"/><circle class="factor-icon" cx="0" cy="-285" r="24" role="img" aria-label="Macronutrient diet icon: plate of food"/><text class="factor-label" x="0" y="-175" text-anchor="middle" dominant-baseline="central" transform="rotate(-90 0 -175)">MACRONUTRIENT DIET</text></g>
        <g transform="rotate(78.75)"><use href="#slice-shape" class="slice slice-b"/><circle class="factor-icon" cx="0" cy="-285" r="24" role="img" aria-label="Micronutrients icon: vitamin capsule"/><text class="factor-label" x="0" y="-175" text-anchor="middle" dominant-baseline="central" transform="rotate(-90 0 -175)">MICRONUTRIENTS</text></g>
        <g transform="rotate(101.25)"><use href="#slice-shape" class="slice slice-a"/><circle class="factor-icon" cx="0" cy="-285" r="24" role="img" aria-label="Health habits icon: checklist and meditation"/><text class="factor-label" x="0" y="-175" text-anchor="middle" dominant-baseline="central" transform="rotate(-90 0 -175)">HEALTH HABITS</text></g>
        <g transform="rotate(123.75)"><use href="#slice-shape" class="slice slice-b"/><circle class="factor-icon" cx="0" cy="-285" r="24" role="img" aria-label="Cardiovascular health icon: heart"/><text class="factor-label" x="0" y="-175" text-anchor="middle" dominant-baseline="central" transform="rotate(-90 0 -175)">CV HEALTH</text></g>
        <g transform="rotate(146.25)"><use href="#slice-shape" class="slice slice-a"/><circle class="factor-icon" cx="0" cy="-285" r="24" role="img" aria-label="GI health icon: stomach"/><text class="factor-label" x="0" y="-175" text-anchor="middle" dominant-baseline="central" transform="rotate(-90 0 -175)">GI HEALTH</text></g>
        <g transform="rotate(168.75)"><use href="#slice-shape" class="slice slice-b"/><circle class="factor-icon" cx="0" cy="-285" r="24" role="img" aria-label="Brain health icon: brain"/><text class="factor-label" x="0" y="-175" text-anchor="middle" dominant-baseline="central" transform="rotate(-90 0 -175)">BRAIN HEALTH</text></g>
        <g transform="rotate(191.25)"><use href="#slice-shape" class="slice slice-a"/><circle class="factor-icon" cx="0" cy="-285" r="24" role="img" aria-label="Inflammation icon: flame"/><text class="factor-label" x="0" y="-175" text-anchor="middle" dominant-baseline="central" transform="rotate(90 0 -175)">INFLAMMATION</text></g>
        <g transform="rotate(213.75)"><use href="#slice-shape" class="slice slice-b"/><circle class="factor-icon" cx="0" cy="-285" r="24" role="img" aria-label="Hormone health icon: molecule"/><text class="factor-label" x="0" y="-175" text-anchor="middle" dominant-baseline="central" transform="rotate(90 0 -175)">HORMONE HEALTH</text></g>
        <g transform="rotate(236.25)"><use href="#slice-shape" class="slice slice-a"/><circle class="factor-icon" cx="0" cy="-285" r="24" role="img" aria-label="Stress icon: storm cloud"/><text class="factor-label" x="0" y="-175" text-anchor="middle" dominant-baseline="central" transform="rotate(90 0 -175)">STRESS</text></g>
        <g transform="rotate(258.75)"><use href="#slice-shape" class="slice slice-b"/><circle class="factor-icon" cx="0" cy="-285" r="24" role="img" aria-label="Immunity and cancer prevention icon: shield"/><text class="factor-label" x="0" y="-175" text-anchor="middle" dominant-baseline="central" transform="rotate(90 0 -175)">IMMUNITY</text></g>
        <g transform="rotate(281.25)"><use href="#slice-shape" class="slice slice-a"/><circle class="factor-icon" cx="0" cy="-285" r="24" role="img" aria-label="Detoxification icon: water drop and leaf"/><text class="factor-label" x="0" y="-175" text-anchor="middle" dominant-baseline="central" transform="rotate(90 0 -175)">DETOXIFICATION</text></g>
        <g transform="rotate(303.75)"><use href="#slice-shape" class="slice slice-b"/><circle class="factor-icon" cx="0" cy="-285" r="24" role="img" aria-label="Longevity icon: hourglass"/><text class="factor-label" x="0" y="-175" text-anchor="middle" dominant-baseline="central" transform="rotate(90 0 -175)">LONGEVITY</text></g>
        <g transform="rotate(326.25)"><use href="#slice-shape" class="slice slice-a"/><circle class="factor-icon" cx="0" cy="-285" r="24" role="img" aria-label="Sexual health icon: linked hearts"/><text class="factor-label" x="0" y="-175" text-anchor="middle" dominant-baseline="central" transform="rotate(90 0 -175)">SEXUAL HEALTH</text></g>
        <g transform="rotate(348.75)"><use href="#slice-shape" class="slice slice-b"/><circle class="factor-icon" cx="0" cy="-285" r="24" role="img" aria-label="Aesthetics icon: mirror and sparkle"/><text class="factor-label" x="0" y="-175" text-anchor="middle" dominant-baseline="central" transform="rotate(90 0 -175)">AESTHETICS</text></g>
        <circle class="wheel-hub" cx="0" cy="0" r="58"/>
      </g>
    </svg>

    <div class="brand-name">VITAL PATH</div>
  </main>
</body>
</html>
```